Web-site design for company trading in chemicals & lubricants

We need a standard 5 page web-site designed for our company based in Dubai, UAE.
The web-site should highlight our capacity to store material as well as distribute the same. The products we sell are basic chemicals - packed in bags as well as drums. Bags are big bags - 25 kgs each as well as drums - 200 litres each. We want to highlight the fact that we huge stocks of this material & can deliver by sea & road,
Please use this site as a ref - http://www.torvane-chemicals.co.uk/
Besides this, we need a page dedicated to finished products that we are selling for use in the auto industry - lubricants, motor oils,brake-fluids, greases, coolants etc. This are packed in large drums as well as small cans.
It would be nice if the site could immediately also provide a ref. to our location - Dubai or that we are based in the Middle East.
We will provide our company logo for reference

```html
<!DOCTYPE html>
<html lang="en">
<head>
<meta charset="utf-8">
<title>Kelvor – Chemicals &amp; Lubricants Trading</title>
<link rel="stylesheet" href="https://fonts.googleapis.com/css2?family=PT+Sans:wght@400;700&family=Arimo:wght@400;700&display=swap">
<style>
:root{
  --bg-top:#553320;
  --bg-bottom:#b3932f;
  --page:#ffffff;
  --brand:#5a3a22;
  --gold:#8a7014;
  --gold-light:#b39a3c;
  --gold-dark:#6e5a0e;
  --text:#333333;
  --muted:#555555;
  --panel:#ebe9e9;
  --rule:#9a8a4a;
}
*{box-sizing:border-box;margin:0;padding:0}
html,body{width:930px;height:1200px;overflow:hidden}
body{
  position:relative;
  background:linear-gradient(to bottom,var(--bg-top) 0,#7a5a2a 420px,var(--bg-bottom) 1200px);
  font-family:"PT Sans",Arial,sans-serif;color:var(--text);
}
.abs{position:absolute}
.page{position:absolute;left:77px;top:26px;width:778px;height:1100px;background:var(--page);box-shadow:0 2px 6px rgba(0,0,0,.45)}

/* header */
.brand{left:90px;top:72px;display:flex;align-items:center;gap:12px}
.brand-name{font-family:"PT Sans",sans-serif;font-weight:700;font-size:46px;letter-spacing:3px;color:var(--brand);line-height:1}
.brand-mark{width:34px;height:34px;border-radius:50%;background:var(--gold)}
.search-panel{left:650px;top:40px;width:203px;height:47px;background:linear-gradient(#fafafa,#e2e2e2);border-radius:0 0 4px 4px}
.search-field{left:674px;top:43px;width:128px;height:24px;border:1px solid #bbb;border-radius:6px;background:#fff}
.search-go{left:807px;top:44px;width:28px;height:21px;border-radius:4px;background:linear-gradient(var(--gold-light),var(--gold-dark));color:#fff;font:11px "Arimo",sans-serif;text-align:center;line-height:21px}
.phone{left:655px;top:100px;display:flex;align-items:center;gap:8px}
.phone-icon{width:24px;height:24px;background:var(--gold);border-radius:3px;display:flex;align-items:center;justify-content:center}
.phone-number{font:21px "Arimo",sans-serif;color:var(--gold-dark)}

/* nav */
.nav-band{left:77px;top:139px;width:778px;height:41px;background:linear-gradient(#fff,#f0f0f0);border-bottom:1px solid #ddd}
.nav{left:94px;top:143px;display:flex;list-style:none}
.nav li{height:34px;margin-right:3px;background:linear-gradient(#f4f4f4,#dcdcdc);border-radius:4px 4px 0 0;font:11px "Arimo",sans-serif;color:#333;text-align:center;line-height:34px}
.nav li.active{background:linear-gradient(var(--gold-light),var(--gold-dark));color:#fff}

/* hero */
.hero{left:85px;top:186px;width:764px;height:292px;background:linear-gradient(100deg,#5f88b5 0,#9fb7cf 30%,#dfe3e6 55%,#c8cbcc 75%,#e9eaea 100%)}
.hero-strip{left:77px;top:478px;width:778px;height:11px;background:#e0e2e6}
.hero-caption{left:112px;top:243px;width:336px;height:139px;background:rgba(255,255,255,.42)}
.hero-title{left:140px;top:257px;font:700 24px "PT Sans",sans-serif;color:#fff}
.hero-text{left:137px;top:297px;width:285px;font:14px/20.5px "PT Sans",sans-serif;color:#222}
.arrow{width:34px;height:34px;border-radius:50%;background:#fff;box-shadow:0 1px 3px rgba(0,0,0,.35);display:flex;align-items:center;justify-content:center}

/* sidebar */
.box{left:83px;width:220px;background:linear-gradient(#f6f5f5,var(--panel));border:1px solid #cfcfcf;border-radius:4px}
.box-head{position:absolute;left:5px;top:5px;width:209px;height:32px;background:linear-gradient(var(--gold-light),var(--gold-dark));color:#fff;font:700 12px/30px "PT Sans",sans-serif;padding-left:19px;letter-spacing:.3px}
.field{position:absolute;height:24px;border:1px solid #999;background:#fff}
.btn{position:absolute;background:linear-gradient(#8c6f36,#5a3d1c);color:#fff;border-radius:3px;font:12px "PT Sans",sans-serif;text-align:center}
.sectors{position:absolute;left:16px;top:52px;list-style:none;font:11px/21px "PT Sans",sans-serif;letter-spacing:.3px;color:#222}
.sectors li::before{content:"›";font-weight:700;color:var(--brand);margin-right:11px}
.map{left:83px;top:943px;width:220px;height:167px;background:linear-gradient(135deg,#cfd6e0,#e8e3cf 55%,#d6c9a8);border-radius:3px}

/* main */
.welcome{left:342px;top:509px;font:22px "PT Sans",sans-serif;color:#111}
.welcome span{color:var(--gold)}
.intro{left:349px;top:546px;width:468px;font:11.4px/17.6px "PT Sans",sans-serif;letter-spacing:.25px;color:#333}
.rule{left:350px;width:451px;border-top:1px dotted var(--rule)}
.section-title{font:15px "PT Sans",sans-serif;color:var(--gold)}
.deal-name{font:14px "PT Sans",sans-serif;color:#111}
.small{font:9px/11.5px "Arimo",sans-serif;color:#333}
.more{font:9px "Arimo",sans-serif;color:var(--gold-dark)}
.photo-lube{left:356px;top:716px;width:118px;height:86px;background:linear-gradient(135deg,#8a8f96,#c9b27a 50%,#5c5f64)}
.photo-oil{left:546px;top:715px;width:82px;height:93px;background:linear-gradient(#3a3a3a,#1a1a1a 70%,#d6d6d6 70%)}
.block-title{font:16px "PT Sans",sans-serif;color:#111}
.avatar{width:32px;height:30px;background:#d8d8d8;border-radius:3px}
.date{font:10px "Arimo",sans-serif;color:var(--gold)}
.body-small{font:10px/12.5px "Arimo",sans-serif;color:#333}

/* footer */
.social{top:1145px;width:22px;height:22px;border-radius:50%}
.footer-links{left:493px;top:1146px;font:10.5px "Arimo",sans-serif;color:#fff}
.footer-links span{margin:0 13px}
.copyright{left:532px;top:1172px;font:10.5px "Arimo",sans-serif;color:#fff}
</style>
</head>
<body>
<div class="page"></div>

<header>
  <div class="abs brand"><span class="brand-name">KELVOR</span><span class="brand-mark"></span></div>
  <div class="abs search-panel"></div>
  <div class="abs search-field">
    <svg class="abs" style="left:106px;top:3px" width="16" height="16" viewBox="0 0 16 16"><circle cx="6.5" cy="6.5" r="4.5" fill="none" stroke="#999" stroke-width="1.6"/><line x1="10" y1="10" x2="14" y2="14" stroke="#999" stroke-width="2"/></svg>
  </div>
  <div class="abs search-go">Go</div>
  <div class="abs phone">
    <span class="phone-icon"><svg width="14" height="16" viewBox="0 0 14 16"><path d="M3 1 L6 1 L6 5 L4.5 6 C5 8.5 6 10 8 11.5 L9.5 10.5 L13 12 L13 15 C7 15 1 9 1 3 Z" fill="#fff"/></svg></span>
    <span class="phone-number">257 410 7786</span>
  </div>
</header>

<nav>
  <div class="abs nav-band"></div>
  <ul class="abs nav">
    <li class="active" style="width:83px">HOME</li>
    <li style="width:83px">ABOUT US</li>
    <li style="width:84px">PARTNERS</li>
    <li style="width:83px">LOGISTICS</li>
    <li style="width:117px">BUSINESS FIELDS</li>
    <li style="width:84px">NEWS</li>
    <li style="width:89px">CONTACT US</li>
  </ul>
</nav>

<section>
  <div class="abs hero" role="img" aria-label="Photograph of white chemical storage tanks at a refinery under a blue sky"></div>
  <div class="abs hero-strip"></div>
  <div class="abs hero-caption"></div>
  <h1 class="abs hero-title">LOREM IPSUM DOLOR</h1>
  <p class="abs hero-text">Lorem ipsum dolor sit amet, consectetuer adipiscing elit. Nam nibh. Nunc varius facilisis eros. Sed erat. Curabitur adipiscing luctus massa.</p>
  <div class="abs arrow" style="left:67px;top:310px"><svg width="12" height="12" viewBox="0 0 12 12"><path d="M9 1 L2 6 L9 11 Z" fill="#bbb"/></svg></div>
  <div class="abs arrow" style="left:830px;top:310px"><svg width="12" height="12" viewBox="0 0 12 12"><path d="M3 1 L10 6 L3 11 Z" fill="#bbb"/></svg></div>
</section>

<aside>
  <div class="abs box" style="top:500px;height:153px">
    <div class="box-head">PRODUCT FINDER</div>
    <div class="abs" style="left:24px;top:55px;font:14px 'PT Sans',sans-serif;color:#222">Enter text</div>
    <div class="field" style="left:24px;top:83px;width:167px"></div>
    <div class="btn" style="left:28px;top:116px;width:42px;height:23px;line-height:23px;font-size:13px">Go</div>
  </div>
  <div class="abs box" style="top:666px;height:128px">
    <div class="box-head">MARKET SECTORS</div>
    <ul class="sectors"><li>Coatings, Inks and Adhesives</li><li>Home Care, Industrial</li><li>Haircare</li></ul>
  </div>
  <div class="abs box" style="top:805px;height:128px">
    <div class="box-head">NEWSLETTER</div>
    <div class="field" style="left:22px;top:49px;width:167px"></div>
    <div class="btn" style="left:28px;top:83px;width:85px;height:24px;line-height:24px;font-size:11.5px;letter-spacing:.5px">SUBSCRIBE</div>
  </div>
  <div class="abs map" role="img" aria-label="Street map area for the company location"></div>
</aside>

<main>
  <h2 class="abs welcome">Welcome to <span>KELVOR</span></h2>
  <p class="abs intro">Lorem ipsum dolor sit amet, adipiscing elit. Nam nibh. Nunc varius facilisis eros. Sed erat. In in velit quis arcuornare laoreet. Curabitur adipiscing luctus massa.Integer ut purus ac commodo commodo. Lorem ipsum dolor sit amet, adipiscing elit. Nam nibh. Nunc varius facilisis eros. Sed erat.In in velit quis arcuornare laoreet. Curabitur adipiscing luctus massa. Integer ut purus ac commodo commodo.</p>
  <div class="abs rule" style="top:650px"></div>

  <h3 class="abs section-title" style="left:353px;top:660px">Our Deals</h3>
  <div class="abs deal-name" style="left:355px;top:689px">Lubricants</div>
  <div class="abs deal-name" style="left:549px;top:689px">Motor Oils</div>
  <div class="abs deal-name" style="left:719px;top:689px">Coolants</div>
  <div class="abs photo-lube" role="img" aria-label="Photograph of oil being poured into an engine"></div>
  <div class="abs photo-oil" role="img" aria-label="Illustration of a motor oil can"></div>
  <p class="abs small" style="left:356px;top:814px;width:130px">Lorem Ipsum is simply dummy text Lorem Ipsum is simply</p>
  <p class="abs small" style="left:543px;top:814px;width:130px">Lorem Ipsum is simply dummy text Lorem Ipsum is simply</p>
  <p class="abs small" style="left:713px;top:814px;width:130px">Lorem Ipsum is simply dummy text Lorem Ipsum is simply</p>
  <a class="abs more" style="left:358px;top:843px">&gt;&gt; More</a>
  <a class="abs more" style="left:547px;top:843px">&gt;&gt; More</a>
  <a class="abs more" style="left:717px;top:843px">&gt;&gt; More</a>
  <div class="abs rule" style="top:884px"></div>

  <h3 class="abs block-title" style="left:368px;top:916px">Testimonials</h3>
  <div class="abs avatar" style="left:362px;top:955px" role="img" aria-label="Customer portrait placeholder"></div>
  <p class="abs body-small" style="left:407px;top:955px;width:150px">Lorem Ipsum is simply dummy text Lorem Ipsum is simplyLorem Ipsum is simply dummy</p>
  <a class="abs more" style="left:409px;top:998px">&gt;&gt; More</a>
  <div class="abs avatar" style="left:364px;top:1032px" role="img" aria-label="Customer portrait placeholder"></div>
  <p class="abs body-small" style="left:407px;top:1032px;width:150px">Lorem Ipsum is simply dummy text Lorem Ipsum is simplyLorem Ipsum is simply dummy</p>
  <a class="abs more" style="left:409px;top:1075px">&gt;&gt; More</a>

  <h3 class="abs block-title" style="left:657px;top:916px">Latest News</h3>
  <div class="abs date" style="left:659px;top:948px">Oct 15, 2011</div>
  <p class="abs body-small" style="left:659px;top:964px;width:150px">Lorem Ipsum is simply dummy text Lorem Ipsum is simplyLorem Ipsum is simply dummy</p>
  <a class="abs more" style="left:662px;top:1008px">&gt;&gt; More</a>
  <div class="abs date" style="left:663px;top:1041px">Oct 15, 2011</div>
  <p class="abs body-small" style="left:663px;top:1057px;width:150px">Lorem Ipsum is simply dummy text Lorem Ipsum is simplyLorem Ipsum is simply dummy</p>
  <a class="abs more" style="left:666px;top:1101px">&gt;&gt; More</a>
</main>

<footer>
  <span class="abs social" style="left:93px;background:#2a4f8f"></span>
  <span class="abs social" style="left:124px;background:#3a9fd6"></span>
  <span class="abs social" style="left:159px;background:#2a6fa8"></span>
  <span class="abs social" style="left:191px;background:#e07a2a"></span>
  <div class="abs footer-links">Privacy Policy<span>|</span>Terms &amp; Conditions<span>|</span>Contact Us</div>
  <div class="abs copyright">Copyright © Kelvor , All Rights Reserved</div>
</footer>
</body>
</html>
```